Webdesign für Entwickler von onlinebasierten Terminformularen
Zielgruppe
Deutsch:
Wir sind ein Startup, das über die Seite Buchwerk.de zukünftig folgenden Service anbietet: Unternehmer können sehr flexibel (selbst) gestaltete Terminformulare erstellen und auf Ihrer Website einbinden. Kunden können dann diese Termine buchen und bekommen dann Erinnerungs-Mails und SMS.
Zielgruppe: Dienstleister wie Fotografen, Friseure, Versicherungsvertreter, Masseure, Restaurants, Arztpraxen. Also alle, die darauf angewiesen sind, dass vereinbarte Termine eingehalten werden und die die Terminvereinbarung vereinfachen wollen. Also weniger per Telefon, mehr über die eigene Website.
Englisch:
We are a start up, that is going to offer this services on the Website Buchwerk.de :
Companies can create highly flexible (self-designed) appointment forms and integrate them on their website. Customer can book appointments and will get an reminding email and SMS.
Target group: Service providers such as photographers, hairdressers, insurance agents, masseurs, restaurants, medical offices. So all those who depend on meeting agreed appointments and who want to simplify the appointment. Less by telephone, more over their own website.
Aufgabenstellung
Übersichtlichkeit, genug Weißraum, deutliche, große Überschriften, Seriös aber gerne frische Farben bei einzelnen Elementen (z.B. bei Icons oder bei Handlungsaufforderungs-Buttons), Trennlinien, Inhalte auf den Punkt.
Logo-Entwurf anbei (wird gerade hier über entwurfsmarkt.de ebenfalls erstellt/optimiert, siehe #418276) sagt das wesentliche aus.
Buchwerk soll also ein sehr nützliches Tool sein, das jeder schnell versteht. Daher muss auch die Website sehr übersichtlich und klar aufgebaut werden. Die wesentlichen Aussagen/Menüpunkte finden sich auf der Startseite (bzw. im Hauptmenü, siehe grober Entwurf anbei).
- frische Farben (z.B. grün, orange, gelb)
- seröse Farben/Grauwerte (z.B. blau, grau, schwarz)
- Hauptmenü/Metanavigation/Footer-Bereich
Das Design und das Teaser-Bild (Frau mit Hammer) auf dem Entwurf anbei (seite1_mit_teaser_entwurf2.jpg) sind nur als grobe Ideen (Richtung) zu verstehen. Die Startseite muss also keine Teaser-Bilder enthalten.
Der Entwurf anbei soll lediglich die ungefähre Richtung mit den angedachten Menüpunkten verdeutlichen.
Übersichtlich und modern finden wir z.B. https://talkrunde.com/de (viel Weißraum, farbige Icons, Infos übersichtlich dargeboten, lächelnde Gesichter) und übrigens auch https://www.entwurfsmarkt.de.
Bitte entwerfen Sie (erstmal) drei Seiten:
- Startseite
- Funktionen/Preis (Beispiel auf https://talkrunde.com/de/tools Und/oder in Tabellenform wie auf https://talkrunde.com/de/pricing/ siehe Content-Plan anbei)
- Über Buchwerk (Über uns, siehe Content-Plan anbei)
Der Content-Plan soll das Projekt verdeutlichen.
Anmerkung von unserem Programmierer: Praktisch wäre eine Basis auf Bootstrap. Dies ist aber keine Pflicht! Das Design/die Idee geht vor :-)
1zu1-Folgeaufträge (für dieses und andere Projekte im Bereich Webdesign, Flyer, CorporateDesign, Grafiken) sind sehr wahrsc..

```html
<!DOCTYPE html>
<html lang="de">
<head>
<meta charset="utf-8">
<title>Buchwerk – Termine online anbieten</title>
<link rel="stylesheet" href="https://fonts.googleapis.com/css2?family=Montserrat:ital,wght@0,300;0,400;0,500;0,600;0,700;1,400&display=swap">
<style>
:root{
  --orange:#f39c1b;
  --navy:#2c3a4b;
  --text:#4a5563;
  --muted:#8d949c;
  --hero:#e8ebed;
  --line:#d9dde1;
  --green:#2ecc71;
  --grey-check:#c5c9ce;
  --white:#ffffff;
}
*{margin:0;padding:0;box-sizing:border-box}
html,body{width:1200px;height:3712px;overflow:hidden}
body{position:relative;background:var(--white);font-family:'Montserrat',sans-serif;color:var(--navy)}
.abs{position:absolute}
a{color:inherit;text-decoration:none}

.topbar{left:0;top:0;width:1200px;height:13px;background:var(--orange);font-size:9px;color:#fff;line-height:13px}
.topbar .tool{left:53px}
.topbar .tool b{color:var(--navy)}
.topbar .meta{right:60px;display:flex;gap:34px}

.logo{font-weight:700;font-size:22px;color:var(--navy)}
.mainnav{top:50px;left:513px;font-size:15px;color:var(--text)}
.mainnav a{position:absolute;white-space:nowrap}
.btn-login{left:1027px;top:42px;width:121px;height:37px;border-radius:19px;background:#fff;box-shadow:0 2px 10px rgba(0,0,0,.12);color:var(--orange);font-weight:600;font-size:15px;display:flex;align-items:center;justify-content:center}

.hero{left:0;top:132px;width:1200px;height:484px;background:var(--hero)}
.hero-title{left:202px;top:212px;font-size:46px;font-weight:700;color:var(--navy);white-space:nowrap}
.hero-title span{color:var(--orange)}
.hero-sub{left:200px;top:280px;font-size:35px;font-weight:300;color:var(--navy);letter-spacing:.3px;white-space:nowrap}
.hero-lead{left:203px;top:360px;font-size:19px;line-height:29px;color:var(--navy)}
.btn-primary{left:203px;top:474px;width:219px;height:44px;border-radius:22px;background:var(--orange);color:#fff;font-weight:600;font-size:18px;display:flex;align-items:center;justify-content:center}
.hero-art{left:800px;top:187px;width:258px;height:382px;border-radius:30px;background:linear-gradient(160deg,#c3c3d6 0%,#b9b9cf 45%,#e79326 60%,#a8742e 100%);opacity:.9}

.feature{width:242px;height:286px;top:710px;background:#fff;box-shadow:0 3px 12px rgba(0,0,0,.1);text-align:center}
.feature .icon{position:absolute;left:78px;top:36px;width:86px;height:86px;border:1.5px solid var(--orange);border-radius:50%;display:flex;align-items:center;justify-content:center}
.feature h3{position:absolute;top:144px;left:0;width:100%;font-size:18px;font-weight:600}
.feature p{position:absolute;top:186px;left:30px;right:30px;font-size:15px;line-height:20px;color:var(--text)}

.section-title{font-size:37px;font-weight:700;color:var(--navy)}
.quote{left:250px;width:700px;top:1236px;text-align:center;font-style:italic;font-size:19px;line-height:27px;color:var(--text)}
.avatar{border-radius:50%;background:linear-gradient(135deg,#6b6f75,#b9a38e)}
.person{left:400px;width:400px;text-align:center}

.price-card{background:#fff;box-shadow:0 3px 14px rgba(0,0,0,.1)}
.price-card h4{position:absolute;font-size:19px;font-weight:600}
.price{position:absolute;color:var(--orange);font-weight:400;white-space:nowrap}
.price .cur{font-size:20px;vertical-align:top;position:relative;top:4px}
.price .val{font-size:40px}
.price .per{font-size:14px;font-weight:600}
.feat{position:absolute;display:flex;gap:14px;font-size:15px;line-height:16px;color:var(--text)}
.feat svg{flex:none}
.btn-outline{position:absolute;height:37px;border:1.5px solid var(--orange);border-radius:19px;color:var(--orange);font-weight:600;font-size:15px;display:flex;align-items:center;justify-content:center}

.desc h2{font-size:41px;font-weight:700;line-height:42px;color:var(--navy)}
.desc p{font-size:16px;line-height:22.5px;color:var(--text);margin-top:30px}
.mockup{border-radius:16px;background:linear-gradient(180deg,#f4f5f6,#dfe2e5)}

.footnav{top:3584px;font-size:14px;color:#b7bcc2}
.footnav a{position:absolute;white-space:nowrap}
.footnav .active{color:var(--orange);font-weight:600}
.footline{left:205px;top:3626px;width:796px;height:1px;background:var(--line)}
.credit{left:207px;top:3659px;font-size:11px;color:#b7bcc2}
.social{width:22px;height:22px;border-radius:50%;background:#c1c5ca;top:3654px}
</style>
</head>
<body>

<div class="abs topbar">
  <span class="abs tool">Tool by <b>datumkraft.de</b></span>
  <span class="abs meta"><a href="#">Login</a><a href="#">Konto erstellen</a><a href="#">EN</a></span>
</div>

<div class="abs logo" style="left:54px;top:45px">Buchwerk</div>
<nav class="abs mainnav">
  <a style="left:0">Home</a><a style="left:77px">Funktionen</a><a style="left:197px">Preise</a>
  <a style="left:273px">Hilfe</a><a style="left:339px">Über Uns</a><a style="left:442px">Blog</a>
</nav>
<a class="abs btn-login" href="#">Anmelden</a>

<section class="abs hero"></section>
<div class="abs hero-art" role="img" aria-label="Illustration eines Hammers mit orangefarbenem Griff"></div>
<h1 class="abs hero-title">Jetzt Termine <span>erstellen</span></h1>
<div class="abs hero-sub">Einfach, Effektiv, Zuverlässig</div>
<p class="abs hero-lead">Jetzt kostenfrei nutzen und Termine<br>online anbieten.</p>
<a class="abs btn-primary" href="#">Kostenlos testen</a>

<div class="abs feature" style="left:203px">
  <div class="icon"><svg width="38" height="38" viewBox="0 0 38 38" fill="none" stroke="#f39c1b" stroke-width="1.5"><rect x="3" y="5" width="32" height="29"/><line x1="3" y1="12" x2="35" y2="12"/><line x1="11" y1="12" x2="11" y2="34"/><line x1="19" y1="12" x2="19" y2="34"/><line x1="27" y1="12" x2="27" y2="34"/><line x1="3" y1="19" x2="35" y2="19"/><line x1="3" y1="26" x2="35" y2="26"/></svg></div>
  <h3>Terminerinnerungen</h3>
  <p>Lorem ipsum dolor sit amet, consectetur adipiscing elit.</p>
</div>
<div class="abs feature" style="left:481px">
  <div class="icon"><svg width="40" height="40" viewBox="0 0 40 40" fill="none" stroke="#f39c1b" stroke-width="1.5"><circle cx="24" cy="20" r="12"/><circle cx="24" cy="20" r="7"/><circle cx="24" cy="20" r="2.5"/><line x1="4" y1="20" x2="22" y2="20"/><line x1="4" y1="16" x2="9" y2="20"/><line x1="4" y1="24" x2="9" y2="20"/></svg></div>
  <h3>Schnell &amp; Zuverlässig</h3>
  <p>Lorem ipsum dolor sit amet, consectetur adipiscing elit.</p>
</div>
<div class="abs feature" style="left:759px">
  <div class="icon"><svg width="40" height="40" viewBox="0 0 40 40" fill="none" stroke="#f39c1b" stroke-width="1.5"><rect x="6" y="6" width="26" height="18"/><line x1="3" y1="27" x2="24" y2="27"/><rect x="24" y="17" width="12" height="18"/><rect x="6" y="27" width="10" height="8"/></svg></div>
  <h3>Auf jedem Gerät</h3>
  <p>Lorem ipsum dolor sit amet, consectetur adipiscing elit.</p>
</div>

<h2 class="abs section-title" style="left:0;width:1206px;text-align:center;top:1174px">Super Tool</h2>
<p class="abs quote">“Im Salon iste die Schere mein Werkzeug. An Buchwerk mag ich<br>besonders die automatische Termin-Erinnerung per SMS und Email<br>für meine Kunden.”</p>
<svg class="abs" style="left:320px;top:1381px" width="28" height="18" viewBox="0 0 28 18" fill="none" stroke="#6b7480" stroke-width="1.6"><line x1="2" y1="9" x2="26" y2="9"/><polyline points="9,2 2,9 9,16"/></svg>
<svg class="abs" style="left:852px;top:1381px" width="28" height="18" viewBox="0 0 28 18" fill="none" stroke="#6b7480" stroke-width="1.6"><line x1="2" y1="9" x2="26" y2="9"/><polyline points="19,2 26,9 19,16"/></svg>
<div class="abs avatar" style="left:394px;top:1365px;width:50px;height:50px" role="img" aria-label="Kundenfoto"></div>
<div class="abs avatar" style="left:480px;top:1365px;width:50px;height:50px" role="img" aria-label="Kundenfoto"></div>
<div class="abs avatar" style="left:568px;top:1358px;width:64px;height:64px;background:linear-gradient(135deg,#3a2a22,#c26a2a)" role="img" aria-label="Foto von Hanna, Friseurin"></div>
<div class="abs avatar" style="left:668px;top:1365px;width:50px;height:50px" role="img" aria-label="Kundenfoto"></div>
<div class="abs avatar" style="left:757px;top:1365px;width:50px;height:50px" role="img" aria-label="Kundenfoto"></div>
<div class="abs person" style="top:1438px;font-size:19px;font-weight:600">Hanna</div>
<div class="abs person" style="top:1465px;font-size:13px;color:var(--muted)">Friseurin aus Heilbronn</div>

<h2 class="abs section-title" style="left:205px;top:1630px;font-size:41px">Unsere Preise</h2>

<div class="abs price-card" style="left:204px;top:1741px;width:241px;height:446px">
  <h4 style="left:32px;top:34px">Lorem Ipsum</h4>
  <div class="price" style="left:30px;top:68px"><span class="cur">€</span><span class="val">9,99</span> <span class="per">pro Monat</span></div>
  <div class="feat" style="left:30px;top:140px"><svg width="18" height="18"><circle cx="9" cy="9" r="9" fill="#2ecc71"/><polyline points="5,9 8,12 13,6" fill="none" stroke="#fff" stroke-width="2"/></svg><span>Lorem ipsum dolor<br>sit amet</span></div>
  <div class="feat" style="left:30px;top:195px"><svg width="18" height="18"><circle cx="9" cy="9" r="9" fill="#2ecc71"/><polyline points="5,9 8,12 13,6" fill="none" stroke="#fff" stroke-width="2"/></svg><span>Lorem ipsum dolor<br>sit amet</span></div>
  <div class="feat" style="left:30px;top:253px"><svg width="18" height="18"><circle cx="9" cy="9" r="9" fill="#c5c9ce"/><polyline points="5,9 8,12 13,6" fill="none" stroke="#fff" stroke-width="2"/></svg><span>Lorem ipsum dolor<br>sit amet</span></div>
  <div class="feat" style="left:30px;top:307px"><svg width="18" height="18"><circle cx="9" cy="9" r="9" fill="#c5c9ce"/><polyline points="5,9 8,12 13,6" fill="none" stroke="#fff" stroke-width="2"/></svg><span>Lorem ipsum dolor<br>sit amet</span></div>
  <a class="btn-outline" href="#" style="left:29px;top:374px;width:183px">Jetzt anmelden</a>
</div>

<div class="abs price-card" style="left:474px;top:1724px;width:258px;height:479px">
  <h4 style="left:34px;top:38px">Lorem Ipsum</h4>
  <div class="price" style="left:30px;top:76px"><span class="cur">€</span><span class="val">14,99</span><span class="per">pro Monat</span></div>
  <div class="feat" style="left:33px;top:152px"><svg width="18" height="18"><circle cx="9" cy="9" r="9" fill="#2ecc71"/><polyline points="5,9 8,12 13,6" fill="none" stroke="#fff" stroke-width="2"/></svg><span>Lorem ipsum dolor<br>sit amet</span></div>
  <div class="feat" style="left:33px;top:211px"><svg width="18" height="18"><circle cx="9" cy="9" r="9" fill="#2ecc71"/><polyline points="5,9 8,12 13,6" fill="none" stroke="#fff" stroke-width="2"/></svg><span>Lorem ipsum dolor<br>sit amet</span></div>
  <div class="feat" style="left:33px;top:272px"><svg width="18" height="18"><circle cx="9" cy="9" r="9" fill="#2ecc71"/><polyline points="5,9 8,12 13,6" fill="none" stroke="#fff" stroke-width="2"/></svg><span>Lorem ipsum dolor<br>sit amet</span></div>
  <div class="feat" style="left:33px;top:331px"><svg width="18" height="18"><circle cx="9" cy="9" r="9" fill="#2ecc71"/><polyline points="5,9 8,12 13,6" fill="none" stroke="#fff" stroke-width="2"/></svg><span>Lorem ipsum dolor<br>sit amet</span></div>
  <a class="btn-outline" href="#" style="left:31px;top:403px;width:197px">Jetzt anmelden</a>
</div>

<div class="abs price-card" style="left:759px;top:1741px;width:241px;height:446px">
  <h4 style="left:32px;top:34px">Lorem Ipsum</h4>
  <div class="price" style="left:28px;top:68px"><span class="cur">€</span><span class="val">4,99</span> <span class="per">pro Monat</span></div>
  <div class="feat" style="left:30px;top:140px"><svg width="18" height="18"><circle cx="9" cy="9" r="9" fill="#2ecc71"/><polyline points="5,9 8,12 13,6" fill="none" stroke="#fff" stroke-width="2"/></svg><span>Lorem ipsum dolor<br>sit amet</span></div>
  <div class="feat" style="left:30px;top:195px"><svg width="18" height="18"><circle cx="9" cy="9" r="9" fill="#c5c9ce"/><polyline points="5,9 8,12 13,6" fill="none" stroke="#fff" stroke-width="2"/></svg><span>Lorem ipsum dolor<br>sit amet</span></div>
  <div class="feat" style="left:30px;top:253px"><svg width="18" height="18"><circle cx="9" cy="9" r="9" fill="#c5c9ce"/><polyline points="5,9 8,12 13,6" fill="none" stroke="#fff" stroke-width="2"/></svg><span>Lorem ipsum dolor<br>sit amet</span></div>
  <div class="feat" style="left:30px;top:307px"><svg width="18" height="18"><circle cx="9" cy="9" r="9" fill="#c5c9ce"/><polyline points="5,9 8,12 13,6" fill="none" stroke="#fff" stroke-width="2"/></svg><span>Lorem ipsum dolor<br>sit amet</span></div>
  <a class="btn-outline" href="#" style="left:29px;top:374px;width:183px">Jetzt anmelden</a>
</div>

<div class="abs desc" style="left:219px;top:2472px;width:290px">
  <h2>Beschreibung vom Tool.</h2>
  <p>Lorem ipsum dolor sit amet, consectetur adipiscing elit, sed do eiusmod tempor incididunt ut labore et dolore magna aliqua. Ut enim ad minim veniam.</p>
</div>
<div class="abs mockup" style="left:622px;top:2386px;width:295px;height:411px" role="img" aria-label="Tablet-Ansicht der Startseite"></div>

<div class="abs mockup" style="left:281px;top:2959px;width:281px;height:432px" role="img" aria-label="Tablet auf Holzständer mit der Startseite"></div>
<div class="abs desc" style="left:639px;top:3042px;width:300px;text-align:right">
  <h2>Beschreibung vom Tool.</h2>
  <p>Lorem ipsum dolor sit amet, consectetur adipiscing elit, sed do eiusmod tempor incididunt ut labore et dolore magna aliqua. Ut enim ad minim veniam.</p>
</div>

<div class="abs logo" style="left:207px;top:3580px;font-size:19px">Buchwerk</div>
<nav class="abs footnav" style="left:500px">
  <a class="active" style="left:0">Home</a><a style="left:70px">Funktionen</a><a style="left:177px">Preise</a>
  <a style="left:246px">Hilfe</a><a style="left:305px">Impressum</a><a style="left:415px">Datenschutz</a>
</nav>
<div class="abs footline"></div>
<div class="abs credit">Tool by <b>datumkraft.de</b></div>
<div class="abs social" style="left:827px" aria-label="Social-Kanal 1"></div>
<div class="abs social" style="left:882px" aria-label="Social-Kanal 2"></div>
<div class="abs social" style="left:937px" aria-label="Social-Kanal 3"></div>
<div class="abs social" style="left:983px" aria-label="Social-Kanal 4"></div>

</body>
</html>
```